Professional Services (B-2-B) Business Cards (Front & Back)

Corvantis is a business-to-business professional services company in the legal sector. They typically present to c-suite and executive functions who are looking for providers with expertise, and experience. Our business card should look and feel professional and contemporary, but we are not a startup tech company, so we want the tone to be more mature.

```html
<!DOCTYPE html>
<html lang="en">
<head>
<meta charset="UTF-8">
<title>Corvantis Business Cards – Front &amp; Back</title>
<link rel="stylesheet" href="https://fonts.googleapis.com/css2?family=Montserrat:wght@400;500;700&display=swap">
<style>
  :root {
    --navy: #1f3466;
    --navy-text: #1f3466;
    --ink-soft: #5f6674;
    --paper: #f7f7f6;
    --backdrop: #c3c6cb;
    --rule: #cfd2d8;
    --white: #ffffff;
  }
  * { margin: 0; padding: 0; box-sizing: border-box; }
  html, body {
    width: 1200px; height: 857px; overflow: hidden;
    background: var(--backdrop);
    font-family: "Montserrat", sans-serif;
  }
  .sheet {
    width: 1200px; height: 857px;
    display: flex; align-items: center; justify-content: center; gap: 60px;
  }
  .card {
    position: relative;
    width: 520px; height: 297px;
    overflow: hidden;
  }
  /* Front */
  .card--front { background: var(--paper); color: var(--navy-text); }
  .brand { position: absolute; left: 40px; top: 112px; }
  .brand__name { font-size: 40px; font-weight: 700; letter-spacing: -0.5px; line-height: 1; }
  .brand__tagline { font-size: 9.5px; font-weight: 500; color: var(--ink-soft); margin-top: 6px; padding-left: 22px; }
  .divider {
    position: absolute; left: 290px; top: 46px;
    width: 1px; height: 176px; background: var(--rule);
  }
  .contact { position: absolute; left: 312px; top: 56px; }
  .contact__name { font-size: 17px; font-weight: 700; line-height: 1.1; }
  .contact__title { font-size: 10.5px; color: var(--ink-soft); margin-bottom: 12px; }
  .contact__list { list-style: none; }
  .contact__item {
    display: flex; align-items: center; gap: 8px;
    font-size: 10.5px; color: var(--ink-soft); line-height: 1.75;
  }
  .contact__item svg { width: 9px; height: 9px; fill: var(--navy); flex: none; }
  .address {
    position: absolute; left: 150px; bottom: 22px;
    font-size: 10px; color: var(--ink-soft);
  }
  .rule { position: absolute; height: 1px; background: var(--navy); opacity: .7; }
  .rule--front-left { left: 30px; bottom: 27px; width: 100px; }
  .rule--front-right { right: 28px; top: 236px; width: 90px; }
  /* Back */
  .card--back { background: var(--navy); color: var(--white); }
  .lockup {
    position: absolute; left: 0; right: 0; top: 118px;
    display: flex; align-items: center; justify-content: center; gap: 18px;
  }
  .lockup__mark { width: 14px; height: 14px; background: var(--white); }
  .lockup__name { font-size: 22px; font-weight: 500; letter-spacing: 9px; }
  .web { position: absolute; right: 34px; bottom: 30px; font-size: 11px; letter-spacing: .3px; }
  .rule--back { background: var(--white); opacity: .55; }
  .rule--back-right { right: 34px; top: 200px; width: 160px; }
  .rule--back-left { left: 150px; bottom: 36px; width: 150px; }
</style>
</head>
<body>
<main class="sheet">
  <section class="card card--front" aria-label="Business card front">
    <div class="brand">
      <div class="brand__name">Corvantis</div>
      <div class="brand__tagline">Programmatic professional services</div>
    </div>
    <div class="divider"></div>
    <div class="contact">
      <div class="contact__name">Lena Morrow</div>
      <div class="contact__title">President &amp; CEO</div>
      <ul class="contact__list">
        <li class="contact__item">
          <svg viewBox="0 0 10 10" aria-hidden="true"><path d="M2 0.5 L3.6 2.6 L2.7 3.6 Q3.8 5.9 6.3 7.2 L7.3 6.3 L9.5 7.9 L8.4 9.5 Q1.2 8.3 0.5 1.6 Z"/></svg>
          (312) 555 – 0184
        </li>
        <li class="contact__item">
          <svg viewBox="0 0 10 10" aria-hidden="true"><path d="M2 0.5 L3.6 2.6 L2.7 3.6 Q3.8 5.9 6.3 7.2 L7.3 6.3 L9.5 7.9 L8.4 9.5 Q1.2 8.3 0.5 1.6 Z"/></svg>
          (312) 555 – 0367
        </li>
        <li class="contact__item">
          <svg viewBox="0 0 10 10" aria-hidden="true"><path d="M0.5 2 H9.5 V8 H0.5 Z M1 2.4 L5 5.4 L9 2.4 V2.9 L5 5.9 L1 2.9 Z" fill-rule="evenodd"/></svg>
          lmorrow@corvantis.tech
        </li>
        <li class="contact__item">
          <svg viewBox="0 0 10 10" aria-hidden="true"><circle cx="5" cy="5" r="4.5"/></svg>
          www.corvantis.tech
        </li>
      </ul>
    </div>
    <div class="rule rule--front-right"></div>
    <div class="rule rule--front-left"></div>
    <div class="address">48 Harbor Row, Suite 210, Eastfield, IN-40112</div>
  </section>

  <section class="card card--back" aria-label="Business card back">
    <div class="lockup">
      <span class="lockup__mark"></span>
      <span class="lockup__name">CORVANTIS</span>
    </div>
    <div class="rule rule--back rule--back-right"></div>
    <div class="rule rule--back rule--back-left"></div>
    <div class="web">www.corvantis.tech</div>
  </section>
</main>
</body>
</html>
```